New business stationairy

I need paper with header and footer and business cards.
I am a Ltd Company and my main field of expertise is QA/QC inspection in the Oil and Gas Industry. I will need all contact detail inserted and a footer with registration number and bank details etc

Industry/Entity Type

Business

```html
<!DOCTYPE html>
<html lang="en">
<head>
<meta charset="utf-8">
<title>Hartwell Inspection Services Ltd. – Business Card</title>
<link rel="stylesheet" href="https://fonts.googleapis.com/css2?family=Mulish:wght@300;400;800&display=swap">
<style>
  :root {
    --backdrop: #e8e8ec;
    --card: #ffffff;
    --brand-blue: #0b4f74;
    --slate-grey: #757479;
    --text-grey: #55565a;
    --band-text: #d9e3ea;
  }
  * { margin: 0; padding: 0; box-sizing: border-box; }
  html, body {
    width: 1200px;
    height: 934px;
    overflow: hidden;
    background: var(--backdrop);
    font-family: "Mulish", sans-serif;
  }
  .business-card {
    position: absolute;
    left: 150px;
    top: 197px;
    width: 900px;
    height: 540px;
    background: var(--card);
    box-shadow: 0 8px 30px rgba(0, 0, 0, 0.12);
    overflow: hidden;
  }
  .corner-block {
    position: absolute;
    left: 0;
    top: 0;
    width: 230px;
    height: 230px;
  }
  .corner-block polygon { fill: var(--slate-grey); }
  .name-band {
    position: absolute;
    left: 246px;
    top: 44px;
    right: 0;
    height: 124px;
    background: var(--brand-blue);
    display: flex;
    align-items: center;
    padding-left: 34px;
  }
  .company-name {
    color: var(--band-text);
    font-weight: 300;
    font-size: 29px;
    letter-spacing: 0.5px;
    text-transform: uppercase;
    white-space: nowrap;
  }
  .holder {
    position: absolute;
    right: 44px;
    top: 196px;
    text-align: right;
  }
  .holder-name {
    color: var(--brand-blue);
    font-weight: 800;
    font-size: 27px;
    letter-spacing: 1px;
    text-transform: uppercase;
    line-height: 1.1;
  }
  .holder-title {
    color: var(--text-grey);
    font-weight: 400;
    font-size: 19px;
    margin-top: 4px;
  }
  .contact {
    position: absolute;
    right: 44px;
    bottom: 56px;
    text-align: right;
    color: var(--text-grey);
    font-size: 19px;
    line-height: 1.35;
  }
  .contact-label {
    color: var(--brand-blue);
    font-weight: 800;
  }
</style>
</head>
<body>
  <main class="business-card">
    <svg class="corner-block" viewBox="0 0 230 230" aria-hidden="true">
      <polygon points="0,0 228,0 200,230 0,230"/>
    </svg>
    <div class="name-band">
      <p class="company-name">Hartwell Inspection Services Ltd.</p>
    </div>
    <div class="holder">
      <h1 class="holder-name">Morag Hartwell</h1>
      <p class="holder-title">Managing Director</p>
    </div>
    <address class="contact" style="font-style: normal;">
      <p>The Willows, Mill Lane, Ashcombe, Blandford, Dorset, DT4 9QP</p>
      <p><span class="contact-label">Phone:</span> +07700 900418 · <span class="contact-label">Email:</span> office@hartwellinspect.co.uk</p>
    </address>
  </main>
</body>
</html>
```